Venture Pathfinders
Name of the Person: Lorena Whitcombe President
Address 427 Maple Ridge Road New York N.Y 10463
Tel: 212 638 2914
Cell: 917 583 21 74
Email:olberinc@quillmail.example

Please use the logo idea of Verantho Change the sense of the arrow do it from right to left
Pantone color for the logo 300 U
For the word strategist use 300U
Please use same fonts or very similar as the one use in Verantho
Please use same lay out as Verantho if you can

Industry/Entity Type

Consulting

Logo Text

Brightmere Advisory

```html
<!DOCTYPE html>
<html lang="en">
<head>
<meta charset="utf-8">
<title>Brightmere Advisory – Business Card</title>
<link href="https://fonts.googleapis.com/css2?family=Arimo:wght@400;700&display=swap" rel="stylesheet">
<style>
  :root {
    --page-bg: #ffffff;
    --card-bg: #ffffff;
    --brand-blue: #1a7fc6;
    --name-grey: #6b6b6b;
    --text-grey: #777777;
    --card-edge: #eeeeee;
    --shadow: rgba(0, 0, 0, 0.45);
  }
  * { box-sizing: border-box; margin: 0; padding: 0; }
  html, body {
    width: 963px;
    height: 1200px;
    overflow: hidden;
    background: var(--page-bg);
    font-family: "Arimo", Arial, sans-serif;
  }
  .business-card {
    position: absolute;
    left: 52px;
    top: 361px;
    width: 860px;
    height: 477px;
    background: var(--card-bg);
    box-shadow: 6px 8px 10px var(--shadow);
    border: 1px solid var(--card-edge);
  }
  .brand {
    position: absolute;
    left: 36px;
    top: 170px;
    display: flex;
    align-items: center;
    gap: 12px;
  }
  .brand-dot {
    width: 16px;
    height: 16px;
    border-radius: 50%;
    background: var(--brand-blue);
  }
  .brand-name {
    font-size: 27px;
    font-weight: 400;
    color: var(--brand-blue);
    letter-spacing: 0.5px;
    white-space: nowrap;
  }
  .person {
    position: absolute;
    right: 46px;
    top: 166px;
    text-align: right;
    font-size: 30px;
    line-height: 34px;
    letter-spacing: 0.5px;
  }
  .person-name { color: var(--name-grey); text-transform: uppercase; }
  .person-title { color: var(--brand-blue); }
  .contact {
    position: absolute;
    left: 36px;
    top: 295px;
    font-size: 22px;
    line-height: 31px;
    color: var(--text-grey);
  }
  .tagline {
    position: absolute;
    right: 46px;
    top: 376px;
    font-size: 18px;
    line-height: 22px;
    text-transform: uppercase;
  }
  .tagline-first { color: var(--text-grey); display: block; text-align: left; }
  .tagline-second { color: var(--brand-blue); display: block; padding-left: 20px; text-align: right; }
</style>
</head>
<body>
  <div class="business-card">
    <div class="brand">
      <span class="brand-dot" aria-hidden="true"></span>
      <span class="brand-name">Brightmere Advisory</span>
    </div>

    <div class="person">
      <div class="person-name">Lorena Whitcombe</div>
      <div class="person-title">President</div>
    </div>

    <div class="contact">
      <div>427 Maple Ridge Road New York N.Y 10463</div>
      <div>Tel. 212 638 2914</div>
      <div>Cell. 917 583 21 74</div>
      <div>Email. olberinc@quillmail.example</div>
    </div>

    <div class="tagline">
      <span class="tagline-first">Venture</span>
      <span class="tagline-second">Pathfinders</span>
    </div>
  </div>
</body>
</html>
```